Tilda and Rook Competition Poster.

Hi Deigners,
I need to help to design a poster for a competition.
Details for competition is exactly the same as my previous design but simply change the name to TILDA & ROOK.
Competition will start : 1st AUGUST 2017
Competion end : 31st AUGUST 2017
Poster name: TILDA & ROOK BREEZE COMPETITION
Poster Description:
WIN a $100 Food Voucher
Share your photos on CHATTERBOX or PHOTOLOOP to WIN.
To Enter, Simply:
1. Like our Chatterbox page or follow us on Photoloop
2. Take an original photo of any item(s) of our food
3. Post your photo(s) to our Chatterbox page or Photoloop page, must use hashtags #tildaandrook #tildaandbreeze
4. Be as creative as you'd like, and the TWO BEST photos voted by the Tilda and Rook team will receive a $100 Food Voucher.
I've also attached the Terms & Conditions, Please Copy and Paste these terms but must replace it with the updated details.
Good Luck everyone

```html
<!DOCTYPE html>
<html lang="en">
<head>
<meta charset="utf-8">
<title>Tilda and Rook Breeze Competition</title>
<link rel="stylesheet" href="https://fonts.googleapis.com/css2?family=Fira+Sans:wght@400;500;600;700;800&display=swap">
<style>
  :root {
    --brown: #8a5a33;
    --orange: #f47a1f;
    --ink: #1c1c1c;
    --panel: rgba(52, 58, 61, 0.86);
    --panel-text: #eceeef;
    --muted: #6d6d6d;
    --sky-top: #e9f6f8;
    --sky-mid: #bfe3e8;
    --sea: #7fc3cc;
  }
  * { box-sizing: border-box; margin: 0; padding: 0; }
  html, body { width: 966px; height: 1200px; overflow: hidden; background: #ffffff; }
  body { font-family: "Fira Sans", Arial, sans-serif; }

  .poster {
    position: relative;
    width: 966px;
    height: 1200px;
    overflow: hidden;
  }
  .backdrop {
    position: absolute;
    inset: 0;
    background:
      radial-gradient(ellipse 420px 380px at 760px 920px, rgba(214, 180, 120, 0.55), rgba(214, 180, 120, 0) 70%),
      radial-gradient(ellipse 220px 300px at 720px 830px, rgba(40, 60, 70, 0.35), rgba(40, 60, 70, 0) 75%),
      linear-gradient(180deg, var(--sky-top) 0%, #f4fafb 30%, var(--sky-mid) 60%, var(--sea) 100%);
  }

  .headline {
    position: absolute;
    left: 0; right: 0;
    top: 56px;
    text-align: center;
    font-weight: 700;
    font-size: 46px;
    letter-spacing: 0.2px;
    color: var(--brown);
  }
  .prize {
    position: absolute;
    left: 0; right: 0;
    top: 124px;
    text-align: center;
    font-weight: 600;
    font-size: 77px;
    line-height: 1;
    color: var(--orange);
  }
  .prize strong { font-weight: 800; }

  .share {
    position: absolute;
    left: 37px;
    top: 215px;
    font-weight: 600;
    font-size: 35px;
    line-height: 47px;
    color: var(--orange);
  }

  .entry {
    position: absolute;
    left: 35px;
    top: 328px;
    width: 600px;
    color: var(--ink);
  }
  .entry-title { font-weight: 600; font-size: 25px; line-height: 32px; margin-bottom: 6px; }
  .entry-steps { list-style: none; padding-left: 20px; font-size: 18.5px; line-height: 24px; }
  .entry-steps li { display: flex; }
  .entry-steps .num { font-weight: 700; width: 22px; flex: none; }

  .brand {
    position: absolute;
    left: 648px;
    top: 372px;
    width: 260px;
    text-align: center;
  }
  .brand-dot {
    width: 64px; height: 64px;
    border-radius: 50%;
    background: var(--orange);
    margin: 0 auto 14px;
  }
  .brand-name { font-weight: 600; font-size: 40px; line-height: 44px; color: var(--orange); }
  .brand-tag { font-size: 16px; letter-spacing: 1px; color: var(--muted); margin-top: 4px; }

  .dates {
    position: absolute;
    left: 580px;
    top: 548px;
    width: 396px;
    text-align: center;
    font-weight: 600;
    font-size: 18px;
    line-height: 24px;
    color: var(--brown);
  }

  .terms {
    position: absolute;
    left: 16px;
    top: 536px;
    width: 533px;
    height: 643px;
    background: var(--panel);
    border-top-right-radius: 56px;
    padding: 16px 0 0 19px;
  }
  .terms-title { font-weight: 600; font-size: 18px; line-height: 24px; color: var(--orange); margin-bottom: 2px; }
  .terms-body p { font-size: 13.4px; line-height: 17px; color: var(--panel-text); }
  .terms-body p + p { margin-top: 17px; }
  .terms-body p.tight { margin-top: 0; }
</style>
</head>
<body>
<main class="poster">
  <div class="backdrop" role="img" aria-label="Soft-focus photo of a hand holding a smartphone, photographing a plate of tacos on a pale turquoise wooden table"></div>

  <h1 class="headline">TILDA &amp; ROOK BREEZE COMPETITION</h1>
  <p class="prize">WIN a <strong>$100</strong> Food Voucher</p>
  <p class="share">Share your photos on<br>CHATTERBOX or PHOTOLOOP to WIN.</p>

  <section class="entry">
    <h2 class="entry-title">To Enter, Simply:</h2>
    <ol class="entry-steps">
      <li><span class="num">1.</span><span>Like our Chatterbox page or follow us on Photoloop</span></li>
      <li><span class="num">2.</span><span>Take an original photo of any item(s) of our food</span></li>
      <li><span class="num">3.</span><span>Post your photo(s) to our Chatterbox page or Photoloop page, must use hashtags #tildaandrook #tildaandbreeze</span></li>
      <li><span class="num">4.</span><span>Be as creative as you'd like, and the TWO BEST photos voted by the Tilda and Rook team will receive a $100 Food Voucher.</span></li>
    </ol>
  </section>

  <div class="brand">
    <div class="brand-dot"></div>
    <p class="brand-name">Sola Kitchen</p>
    <p class="brand-tag">No1 Vietnamese Phở</p>
  </div>

  <p class="dates">Runs 1st – 31st AUGUST 2017</p>

  <section class="terms">
    <h2 class="terms-title">Terms &amp; conditions</h2>
    <div class="terms-body">
      <p>Lorem Ipsum is simply dummy text of the printing and typesetting industry.<br>Lorem Ipsum has been the industry's standard dummy text ever since the 1500s,<br>when an unknown printer took a galley of type and scrambled it to make a type<br>specimen book. It has survived not only five centuries, but also the leap into<br>electronic typesetting, remaining essentially unchanged. It was popularised in<br>the 1960s with the release of Lettrafix sheets containing Lorem Ipsum passages,<br>and more recently with desktop publishing software like Quillpage Studio<br>including versions of Lorem Ipsum.</p>
      <p>Lorem Ipsum is simply dummy text of the printing and typesetting industry.<br>Lorem Ipsum has been the industry's standard dummy text ever since the 1500s,<br>when an unknown printer took a galley of type and scrambled it to make a type<br>specimen book. It has survived not only five centuries, but also the leap into<br>electronic typesetting, remaining essentially unchanged. It was popularised in<br>the 1960s with the release of Lettrafix sheets containing Lorem Ipsum passages,<br>and more recently with desktop publishing software like Quillpage Studio<br>including versions of Lorem Ipsum.</p>
      <p>Lorem Ipsum is simply dummy text of the printing and typesetting industry.<br>Lorem Ipsum has been the industry's standard dummy text ever since the 1500s,<br>when an unknown printer took a galley of type and scrambled it to make a type<br>specimen book. It has survived not only five centuries, but also the leap into<br>electronic typesetting, remaining essentially unchanged. It was popularised in<br>the 1960s with the release of Lettrafix sheets containing Lorem Ipsum passages,<br>and more recently with desktop publishing software like Quillpage Studio<br>including versions of Lorem Ipsum.</p>
      <p class="tight">Lorem Ipsum is simply dummy text of the printing and typesetting industry.<br>Lorem Ipsum has been the industry's standard dummy text ever since the 1500s,<br>when an unknown printer took a galley of type and scrambled it to make a type<br>specimen book. It has survived not only five centuries, but also the leap into<br>electronic typesetting, remaining essentially unchanged. It was popularised in<br>the 1960s with the release of Lettrafix sheets containing Lorem Ipsum passages,<br>and more recently with desktop publishing software like Quillpage Studio<br>including versions of Lorem Ipsum.</p>
    </div>
  </section>
</main>
</body>
</html>
```